Business Card for IT company

I need a high tech looking business card using our logo. I prefer something clean and modern.

Target Market(s)

Buyers of IT hardware and software, IT Techies who are key influencers

Industry/Entity Type

Business

```html
<!DOCTYPE html>
<html lang="en">
<head>
<meta charset="utf-8">
<title>Norvale Consulting – Business Card</title>
<link rel="stylesheet" href="https://fonts.googleapis.com/css2?family=Open+Sans:wght@400;600;700&display=swap">
<style>
  :root {
    --bg: #3a3a3c;
    --card-white: #ffffff;
    --ink: #333333;
    --ink-soft: #555555;
    --green: #3f9b45;
    --green-light: #6cc04a;
    --green-dark: #2f8a3a;
    --divider: #cfcfcf;
  }
  * { margin: 0; padding: 0; box-sizing: border-box; }
  html, body { width: 1200px; height: 1009px; overflow: hidden; }
  body {
    background: var(--bg);
    font-family: "Open Sans", Arial, sans-serif;
    position: relative;
  }
  .card {
    position: absolute;
    width: 620px;
    height: 354px;
    overflow: hidden;
    box-shadow: 0 10px 30px rgba(0,0,0,.45);
  }

  /* Front */
  .card-front { left: 80px; top: 70px; background: var(--card-white); }
  .card-front .bands { position: absolute; inset: 0; }
  .brand-name {
    position: absolute;
    left: 150px; top: 62px;
    font-size: 42px; font-weight: 700;
    color: var(--ink);
    letter-spacing: 1px;
  }
  .holder {
    position: absolute;
    right: 330px; top: 172px;
    text-align: right;
    color: var(--ink);
    font-size: 14px; line-height: 1.35;
  }
  .holder .name { color: var(--green); font-weight: 700; font-size: 21px; }
  .holder .title { margin-bottom: 10px; }
  .divider {
    position: absolute;
    left: 305px; top: 170px;
    width: 1px; height: 100px;
    background: var(--divider);
  }
  .contacts {
    position: absolute;
    left: 322px; top: 172px;
    list-style: none;
    color: var(--ink);
    font-size: 14px; line-height: 1.65;
  }
  .contacts li { display: flex; align-items: center; gap: 8px; }
  .contacts svg { width: 13px; height: 13px; flex: none; }

  /* Back */
  .card-back {
    left: 500px; top: 570px;
    background: radial-gradient(ellipse at 50% 42%, var(--green-light) 0%, var(--green) 55%, var(--green-dark) 100%);
  }
  .back-brand {
    position: absolute;
    left: 0; right: 0; top: 110px;
    text-align: center;
    font-size: 64px; font-weight: 700;
    color: var(--ink);
    letter-spacing: 2px;
  }
  .back-url {
    position: absolute;
    left: 0; right: 0; top: 250px;
    text-align: center;
    color: #ffffff;
    font-size: 17px; font-weight: 600;
    letter-spacing: 4px;
  }
</style>
</head>
<body>

<section class="card card-front" aria-label="Business card front">
  <svg class="bands" viewBox="0 0 620 354" aria-hidden="true">
    <polygon points="0,354 335,300 322,354" fill="#333333"/>
    <polygon points="345,296 620,236 620,354 330,354" fill="#3f9b45"/>
    <polygon points="345,296 620,236 620,244 352,302" fill="#6cc04a"/>
  </svg>

  <div class="brand-name">Norvale Consulting</div>

  <div class="holder">
    <div class="name">Your Name</div>
    <div class="title">Title</div>
    <div>Street Name, City Name</div>
    <div>State, City Zip Code</div>
  </div>

  <div class="divider"></div>

  <ul class="contacts">
    <li>
      <svg viewBox="0 0 14 14"><circle cx="7" cy="7" r="7" fill="#3f9b45"/><path d="M4.5 3.5l1.5 0 .7 2-1 .8c.5 1 1.2 1.7 2.2 2.2l.8-1 2 .7v1.5c-3.5.3-6.5-2.7-6.2-6.2z" fill="#fff"/></svg>
      0123-456-789
    </li>
    <li>
      <svg viewBox="0 0 14 14"><circle cx="7" cy="7" r="7" fill="#3f9b45"/><rect x="5" y="3" width="4" height="8" rx="1" fill="#fff"/></svg>
      0123-456-789
    </li>
    <li>
      <svg viewBox="0 0 14 14"><circle cx="7" cy="7" r="7" fill="#3f9b45"/><rect x="3.5" y="4.5" width="7" height="5" fill="#fff"/><path d="M3.5 4.5l3.5 3 3.5-3" stroke="#3f9b45" stroke-width=".8" fill="none"/></svg>
      info@norvaleconsulting.com
    </li>
    <li>
      <svg viewBox="0 0 14 14"><circle cx="7" cy="7" r="7" fill="#3f9b45"/><circle cx="7" cy="7" r="3.6" fill="none" stroke="#fff" stroke-width=".9"/><path d="M3.4 7h7.2M7 3.4v7.2" stroke="#fff" stroke-width=".8"/></svg>
      www.norvaleconsulting.com
    </li>
  </ul>
</section>

<section class="card card-back" aria-label="Business card back">
  <div class="back-brand">Norvale</div>
  <div class="back-url">www.norvaleconsulting.com</div>
</section>

</body>
</html>
```